Fresh pet feed direct from manufacturer to door step. Quality and Freshness un-surpassed in Industr

Need Business Card Design; leading into many other projects, for New Franchised Business Opportunity providing home delivery of fresh dog and cat feed (no emphasis needed for cat) direct from manufacturing facility. (no middle men or distributors) Food is Farm to Factory fresh. Our trademarked tagline is "Quality is our MAIN Ingredient ! "
Updates

Please take note of other contest for Chirplane Cover and Profile Pic's

Target Market(s)

Dog and Cat owners

Industry/Entity Type

Pet

Contact Information for Business Card

Name, address, local phone, national 800 number, website, email address

Other font styles liked:
• follow that from logo

Requirements
Must have
• Our feed is made in Texas with ingredients sourced from local farms. We want to lean heavy on the Made in West Texas , ranch theme but that has a 'black label', 'vantrel', 'premium', 'high-end' look and feel
Nice to have
• maybe have an offer on card? 20% off with promo code "x" etc.. ?? just a thought...

```html
<!DOCTYPE html>
<html lang="en">
<head>
<meta charset="utf-8">
<title>Hadley's Premium – Business Card</title>
<link href="https://fonts.googleapis.com/css2?family=Zilla+Slab:wght@500;700&display=swap" rel="stylesheet">
<style>
  :root {
    --page-bg: #2a2726;
    --metal-dark: #b98a6c;
    --metal-mid: #e2b99c;
    --metal-light: #f3d7c2;
    --panel-top: #e4d1b0;
    --panel-bottom: #cdb791;
    --ink: #6e6555;
    --ink-soft: #857b69;
  }
  html, body {
    margin: 0;
    width: 1200px;
    height: 1000px;
    overflow: hidden;
    background: var(--page-bg);
  }
  .card {
    position: absolute;
    left: 150px;
    top: 243px;
    width: 900px;
    height: 514px;
    background: linear-gradient(180deg, var(--panel-top), var(--panel-bottom));
    font-family: "Zilla Slab", Georgia, serif;
    color: var(--ink);
    overflow: hidden;
  }
  .metal-band {
    position: absolute;
    left: 0;
    width: 100%;
    height: 92px;
    background:
      repeating-linear-gradient(115deg, rgba(255,255,255,0.10) 0 2px, rgba(0,0,0,0.04) 2px 4px),
      linear-gradient(100deg, var(--metal-dark) 0%, var(--metal-light) 22%, var(--metal-mid) 40%, var(--metal-dark) 58%, var(--metal-light) 78%, var(--metal-mid) 100%);
  }
  .metal-band--top { top: 0; }
  .metal-band--bottom { bottom: 0; }
  .brand {
    position: absolute;
    left: 70px;
    top: 118px;
    display: flex;
    align-items: center;
    gap: 14px;
    font-size: 40px;
    font-weight: 700;
    letter-spacing: 1px;
    text-transform: uppercase;
  }
  .brand-dot {
    width: 28px;
    height: 28px;
    border-radius: 50%;
    background: var(--ink);
  }
  .contact-list {
    position: absolute;
    left: 70px;
    top: 200px;
    margin: 0;
    padding: 0;
    list-style: none;
    font-size: 22px;
    font-weight: 500;
    letter-spacing: 0.5px;
    text-transform: uppercase;
  }
  .contact-list li {
    display: flex;
    align-items: center;
    gap: 16px;
    height: 34px;
  }
  .contact-icon { width: 20px; height: 20px; fill: var(--ink); flex: none; }
  .person {
    position: absolute;
    right: 60px;
    top: 250px;
    text-align: left;
  }
  .person-name {
    margin: 0;
    font-size: 50px;
    font-weight: 700;
    line-height: 1;
    letter-spacing: 1px;
    text-transform: uppercase;
  }
  .person-role {
    margin: 4px 0 0;
    font-size: 20px;
    font-weight: 700;
    letter-spacing: 1.5px;
    color: var(--ink-soft);
    text-transform: uppercase;
  }
  .peak-line {
    position: absolute;
    left: 600px;
    top: 318px;
  }
</style>
</head>
<body>
  <div class="card">
    <div class="metal-band metal-band--top"></div>
    <div class="metal-band metal-band--bottom"></div>

    <div class="brand"><span class="brand-dot"></span>Hadley's Premium</div>

    <ul class="contact-list">
      <li>
        <svg class="contact-icon" viewBox="0 0 24 24"><path d="M6.6 10.8a15 15 0 0 0 6.6 6.6l2.2-2.2a1 1 0 0 1 1-.25 11.4 11.4 0 0 0 3.6.57 1 1 0 0 1 1 1V20a1 1 0 0 1-1 1A17 17 0 0 1 3 4a1 1 0 0 1 1-1h3.5a1 1 0 0 1 1 1c0 1.25.2 2.45.57 3.57a1 1 0 0 1-.25 1z"/></svg>
        1234-580-472 / 800-377-905
      </li>
      <li>
        <svg class="contact-icon" viewBox="0 0 24 24"><path d="M2 5h20v14H2z M4 7v.4l8 5.2 8-5.2V7z" fill-rule="evenodd"/></svg>
        w.corbin@hadleys.com
      </li>
      <li>
        <svg class="contact-icon" viewBox="0 0 24 24"><path d="M12 2a10 10 0 1 0 0 20 10 10 0 0 0 0-20zm0 2c.9 1.2 1.6 2.6 2 4h-4c.4-1.4 1.1-2.8 2-4zM4.3 14a8 8 0 0 1 0-4h3.4a16 16 0 0 0 0 4zm5.7 0a14 14 0 0 1 0-4h4a14 14 0 0 1 0 4zm6.3 0a16 16 0 0 0 0-4h3.4a8 8 0 0 1 0 4zM12 20c-.9-1.2-1.6-2.6-2-4h4c-.4 1.4-1.1 2.8-2 4z"/></svg>
        www.hadleysfeed.com
      </li>
      <li>
        <svg class="contact-icon" viewBox="0 0 24 24"><path d="M12 2a7 7 0 0 0-7 7c0 5 7 13 7 13s7-8 7-13a7 7 0 0 0-7-7zm0 9.5A2.5 2.5 0 1 1 12 6.5a2.5 2.5 0 0 1 0 5z"/></svg>
        Ridgeline Road, Lubbock 7940
      </li>
    </ul>

    <div class="person">
      <p class="person-name">Wade Corbin</p>
      <p class="person-role">General Manager</p>
    </div>

    <svg class="peak-line" width="200" height="110" viewBox="0 0 200 110">
      <polyline points="8,104 160,6 176,104" fill="none" stroke="#8a806c" stroke-width="4" stroke-linejoin="miter"/>
    </svg>
  </div>
</body>
</html>
```